Rw construct holdings pty ltd

This is a development and construction company. Website can be set up on our domain rwbuildgroup.net if we could change the domain to rwbuildgroup.com.au would be great

Want the page to have eye catching designs, red, black and white are the preffered colours.

Check out www.tolumine.com.au it is my former company with my partner which i am now venturing out on my own, that is the perfect example of the website i want even allot of the information would be the same

Industry/Entity Type

Construction

Coding

Coded - Design and coding required

Number of Pages Required

5+ page

Requirements
Must have
• Company logo eye catching designs

```html
<!DOCTYPE html>
<html lang="en">
<head>
<meta charset="utf-8">
<title>RW Construct – Building Your Dream Home</title>
<link href="https://fonts.googleapis.com/css2?family=Roboto:wght@500;700;900&family=Open+Sans:wght@400;600&display=swap" rel="stylesheet">
<style>
:root{
  --red:#ef3224;
  --salmon:#f28a7d;
  --brick:#b9443a;
  --dark:#372c2b;
  --ink:#1d1d1d;
  --grey:#f2f2f2;
  --white:#ffffff;
  --body:#333333;
}
*{box-sizing:border-box;margin:0;padding:0}
html,body{width:1200px;height:4059px;overflow:hidden}
body{font-family:"Open Sans",Arial,sans-serif;color:var(--body);background:var(--white);position:relative}
.wrap{width:712px;margin:0 auto;position:relative}
h1,h2,h3,h4{font-family:"Roboto",Arial,sans-serif}

/* header */
.site-header{height:77px}
.site-header .wrap{display:flex;justify-content:space-between;align-items:center;height:77px}
.brand{display:flex;align-items:center;gap:9px;font-family:"Roboto",Arial,sans-serif;font-weight:700;font-size:17px;letter-spacing:1px;color:var(--ink)}
.brand-dot{width:14px;height:14px;border-radius:50%;background:var(--red)}
.main-nav{display:flex;gap:20px;font-size:11px}
.main-nav a{color:var(--ink);text-decoration:none;padding-bottom:4px}
.main-nav a.active{color:var(--red);border-bottom:2px solid var(--red)}

/* hero */
.hero{height:460px;position:relative;background:linear-gradient(100deg,#9b4f55 0%,#8a5563 40%,#5e5468 70%,#3c4150 100%)}
.hero .wrap{height:460px;text-align:right}
.hero h1{position:absolute;right:0;top:103px;font-weight:700;font-size:64px;line-height:66px;color:var(--white);letter-spacing:1px}
.hero p{position:absolute;right:0;top:386px;font-size:15px;line-height:25px;color:var(--white)}

/* project strip */
.strip{height:235px;background:var(--red);padding-top:33px}
.strip .wrap{display:flex;gap:8px}
.strip .shot{height:169px;flex:1}

.ph{display:block}
.ph-house-a{background:linear-gradient(180deg,#dfe3e6,#8c8f93 70%,#5e6064)}
.ph-house-b{background:linear-gradient(180deg,#7ea6d8,#e4e4e4 50%,#5e8a3b)}
.ph-house-c{background:linear-gradient(180deg,#6f9fd6,#7b7f82 55%,#4c5a4e)}
.ph-living{background:linear-gradient(120deg,#3a3a3c 0%,#ededed 55%,#b76a3f 100%)}
.ph-kitchen{background:linear-gradient(160deg,#f1f1f1,#bdbdbd)}
.ph-kitchen-dark{background:linear-gradient(160deg,#e8e8e8,#4a4a4a)}
.ph-duplex{background:linear-gradient(180deg,#6c9fd8 0%,#8c8c8c 45%,#5e6a63 85%,#6f9a49 100%)}
.ph-dusk{background:linear-gradient(180deg,#4e5d80 0%,#8f8aa3 30%,#cfcfd3 60%,#3b3b40 100%)}
.ph-dusk-b{background:linear-gradient(180deg,#3f5a8d 0%,#c9c9cf 50%,#3b3b3f 100%)}

/* project feature */
.feature-title{text-align:center;font-weight:700;font-size:38px;line-height:46px;color:var(--brick)}
.project-card{display:flex;height:378px}
.project-card > .ph{width:356px;flex-shrink:0}
.project-card .info{flex:1;background:var(--dark);padding:0 38px;display:flex;flex-direction:column;justify-content:center;align-items:flex-start;color:var(--salmon)}
.project-card h3{font-weight:700;font-size:22px;line-height:36px;margin-bottom:14px}
.project-card p{font-size:11px;line-height:18px;margin-bottom:12px}
.project-card a{font-size:10px;color:var(--salmon);text-decoration:none;border-bottom:1px solid var(--salmon);padding-bottom:2px}
.avatar{width:78px;height:78px;flex:0 0 78px;border-radius:50%;margin-bottom:18px}

.feature-first{padding-top:38px}
.feature-first .feature-title{margin-bottom:22px}

/* intro */
.intro{text-align:center;padding-top:92px}
.intro h2{font-weight:700;font-size:37px;line-height:41px;color:var(--red);margin-bottom:22px}
.intro p{width:430px;margin:0 auto;font-size:12.5px;line-height:22.5px;color:var(--ink)}

/* what we do */
.what{position:absolute;top:1625px;left:0;width:1200px;height:457px;background:var(--salmon);padding-top:41px}
.what-card{display:flex;height:377px;background:var(--white)}
.what-card .text{width:356px;padding:0 38px;display:flex;flex-direction:column;justify-content:center;align-items:flex-start;color:var(--red)}
.what-card h3{font-weight:700;font-size:22px;margin-bottom:16px}
.what-card p{font-size:12px;line-height:20px;margin-bottom:12px}
.what-card a{font-size:11px;color:var(--red);text-decoration:none;border-bottom:1px solid var(--red);padding-bottom:2px}
.what-card .grid{flex:1;display:grid;grid-template-columns:1fr 1fr;grid-template-rows:1fr 1fr}

/* values */
.values{position:absolute;top:2082px;left:0;width:1200px;height:229px;background:var(--red)}
.values .wrap{display:flex;height:229px;align-items:center}
.value{flex:1;text-align:center;color:var(--white);font-family:"Roboto",Arial,sans-serif;font-weight:700;font-size:17px;line-height:22px}
.value svg{display:block;margin:0 auto 12px}

/* statement */
.statement{position:absolute;top:2311px;left:0;width:1200px;height:231px;background:var(--grey)}
.statement p{position:absolute;left:250px;top:62px;font-family:"Roboto",Arial,sans-serif;font-weight:700;font-size:22px;line-height:36px;color:var(--ink)}

/* budgets */
.budgets{position:absolute;top:2542px;left:0;width:1200px;height:340px}
.budgets .blurb{position:absolute;left:257px;top:92px;width:165px;font-size:11px;line-height:28px;color:var(--red);text-transform:uppercase}
.budgets .blurb a{display:inline-block;margin-top:16px;color:var(--red);text-decoration:none;border-bottom:1px solid var(--red);line-height:14px}
.budgets .ph{position:absolute;left:517px;top:35px;width:439px;height:271px}

.panorama{position:absolute;top:2882px;left:0;width:1200px;height:310px}

.feature-second{position:absolute;top:3192px;left:0;width:1200px}
.feature-second .feature-title{margin-top:38px;margin-bottom:22px}
.feature-second .project-card{height:374px}

/* cta */
.cta{position:absolute;top:3709px;left:0;width:1200px;height:186px;background:var(--grey);text-align:center}
.cta h2{margin-top:32px;font-weight:700;font-size:23px;color:var(--ink)}
.cta p{width:420px;margin:12px auto 0;font-size:11px;line-height:17px;color:var(--ink)}
.cta a{display:inline-block;margin-top:16px;padding:7px 18px;border:1px solid #666;font-size:10px;letter-spacing:1px;color:#444;text-decoration:none}

/* footer */
.site-footer{position:absolute;top:3895px;left:0;width:1200px;height:164px;background:var(--red);text-align:center;color:var(--white)}
.footer-nav{margin-top:42px;display:flex;justify-content:center;gap:26px;font-size:11px}
.footer-nav a{color:var(--white);text-decoration:none}
.social{margin-top:16px;display:flex;justify-content:center;gap:9px}
.social span{width:10px;height:10px;border-radius:50%;background:var(--white)}
.copyright{margin-top:22px;font-size:10px}
</style>
</head>
<body>

<header class="site-header">
  <div class="wrap">
    <div class="brand"><span class="brand-dot"></span>RW CONSTRUCT</div>
    <nav class="main-nav">
      <a href="#" class="active">Home</a>
      <a href="#">Services</a>
      <a href="#">Projects</a>
      <a href="#">Contact Us</a>
    </nav>
  </div>
</header>

<section class="hero" role="img" aria-label="Modern two-storey duplex at sunset with a red overlay">
  <div class="wrap">
    <h1>BUILDING<br>YOUR<br>DREAM<br>HOME</h1>
    <p>The Perfect Combination of Innovation &amp; Quality<br>for Building Your Dream Home.</p>
  </div>
</section>

<section class="strip">
  <div class="wrap">
    <div class="shot ph ph-house-a" role="img" aria-label="White and grey modern townhouse facade"></div>
    <div class="shot ph ph-house-b" role="img" aria-label="Brick home with timber posts and green lawn"></div>
    <div class="shot ph ph-house-c" role="img" aria-label="Grey cladded duplex under blue sky"></div>
  </div>
</section>

<section class="feature-first">
  <h2 class="feature-title">Brennan St, Corriwood</h2>
  <div class="wrap">
    <div class="project-card">
      <div class="ph ph-living" role="img" aria-label="Living room with dark brick feature wall and leather sofa"></div>
      <div class="info">
        <h3>Architecturally Designed<br>Residence</h3>
        <p>A beautiful brand-new home, defined by its striking facade, this architecturally designed residence exudes undeniable luxury, showcasing exquisite cathedral ceilings, superior craftsmanship and an assortment of the finest inclusions and features.</p>
        <a href="#">See this project</a>
      </div>
    </div>
  </div>
</section>

<section class="intro">
  <h2>Quality, Innovation &amp;<br>Excellence</h2>
  <p>Our commitment to quality and excellence in home design has helped us become the builders we are today. We’ve never been satisfied with simply building homes ‘the way it’s always been done.’ This is what sets our company apart from the rest. In fact, our passion for innovation is at the heart of our business our constant search for innovation is always at our core.</p>
</section>

<section class="what">
  <div class="wrap">
    <div class="what-card">
      <div class="text">
        <h3>What We Do</h3>
        <p>We at RW Construct believe that building your dream home shouldn’t cost your life savings! Nor should it take a lifetime to build!</p>
        <a href="#">See our latest projects</a>
      </div>
      <div class="grid">
        <div class="ph ph-kitchen" role="img" aria-label="White kitchen with pendant lights and bar stools"></div>
        <div class="ph ph-kitchen-dark" role="img" aria-label="Open plan kitchen and dining area"></div>
        <div class="ph ph-kitchen-dark" role="img" aria-label="Kitchen island with timber cabinetry"></div>
        <div class="ph ph-kitchen" role="img" aria-label="Kitchen with dark timber joinery"></div>
      </div>
    </div>
  </div>
</section>

<section class="values">
  <div class="wrap">
    <div class="value">
      <svg width="44" height="44" viewBox="0 0 44 44" fill="none" stroke="#fff" stroke-width="2"><circle cx="17" cy="17" r="11"/><line x1="25" y1="25" x2="38" y2="38" stroke-width="4"/></svg>
      Transparency
    </div>
    <div class="value">
      <svg width="44" height="44" viewBox="0 0 44 44" fill="none" stroke="#fff" stroke-width="2"><circle cx="22" cy="10" r="4"/><circle cx="11" cy="22" r="4"/><circle cx="33" cy="22" r="4"/><circle cx="22" cy="24" r="4"/><path d="M4 38c0-6 3-9 7-9s7 3 7 9M26 38c0-6 3-9 7-9s7 3 7 9M15 40c0-6 3-9 7-9s7 3 7 9"/></svg>
      Leadership
    </div>
    <div class="value">
      <svg width="44" height="44" viewBox="0 0 44 44" fill="none" stroke="#fff" stroke-width="2"><path d="M14 38h16M16 34h12l-2-12 5-3-4-10-7-3-8 8 2 4 5-2z"/></svg>
      Strategic
    </div>
    <div class="value">
      <svg width="44" height="30" viewBox="0 0 44 30" fill="none" stroke="#fff" stroke-width="1.6"><path d="M9 3l2 4 4 .5-3 3 .8 4L9 12.5 5.2 14.5 6 10.5l-3-3 4-.5z"/><path d="M22 3l2 4 4 .5-3 3 .8 4-3.8-2-3.8 2 .8-4-3-3 4-.5z"/><path d="M35 3l2 4 4 .5-3 3 .8 4-3.8-2-3.8 2 .8-4-3-3 4-.5z"/><path d="M15 18l2 4 4 .5-3 3 .8 4-3.8-2-3.8 2 .8-4-3-3 4-.5z"/><path d="M29 18l2 4 4 .5-3 3 .8 4-3.8-2-3.8 2 .8-4-3-3 4-.5z"/></svg>
      Exception<br>Client Service
    </div>
  </div>
</section>

<section class="statement">
  <p>We at RW Construct believe that building your dream home<br>shouldn’t cost your life savings! Nor should it take a lifetime to build!<br>We are determined to make your new build your forever home!</p>
</section>

<section class="budgets">
  <div class="blurb">We create innovative designs and build quality homes, to suit all budgets.<br><a href="#">View projects</a></div>
  <div class="ph ph-duplex" role="img" aria-label="Contemporary grey and white duplex with balconies"></div>
</section>

<div class="panorama ph ph-dusk" role="img" aria-label="Wide view of a lit modern duplex at dusk"></div>

<section class="feature-second">
  <h2 class="feature-title">Tallis Street, Eastmere</h2>
  <div class="wrap">
    <div class="project-card">
      <div class="ph ph-dusk-b" role="img" aria-label="Twin modern homes with garages at twilight"></div>
      <div class="info">
        <div class="avatar ph ph-kitchen" role="img" aria-label="Round thumbnail of an interior"></div>
        <h3>Luxury!</h3>
        <p>Luxury! An architecturally designed stunning 5 bedroom residence. Boasting high end finishes throughout the home from designer kitchen finishes, to floating staircase with LED light steps, this build will be sure to excite the senses.</p>
        <a href="#">See this project</a>
      </div>
    </div>
  </div>
</section>

<section class="cta">
  <h2>Let's build your dream home together!</h2>
  <p>Lorem ipsum dolor sit amet, consectetur adipiscing elit. Mauris suscipit, sem vitae ornare molestie, massa tellus ullamcorper justo.</p>
  <a href="#">CONTACT US</a>
</section>

<footer class="site-footer">
  <nav class="footer-nav">
    <a href="#">Home</a>
    <a href="#">Services</a>
    <a href="#">Projects</a>
    <a href="#">Contact Us</a>
  </nav>
  <div class="social">
    <span aria-label="Social link"></span>
    <span aria-label="Social link"></span>
    <span aria-label="Social link"></span>
    <span aria-label="Social link"></span>
  </div>
  <p class="copyright">RW Construct 2021. All rights reserved.</p>
</footer>

</body>
</html>
```